A Leisure SPA Plaza Hotel needs Creative VIP Cards Design

We need VIP Cards Design for a SPA Plaza Hotel, This leisure SPA plaza hotel have multiple sub projects, such as leisure hotel room, large buffet restaurant, swimming pool, theatrical performances, sauna bath, massage, SPA, Tea bar, 3D cinema, KTV rooms, chess room, Internet cafes , art appreciation, children's Castle, Korean geothermal, table tennis, billiard room, GYM and other entertainments.
We need Three creative VIP Card design for 3 different level:
1. Golden Card
2. Platinum Card
3. Diamond Card
Attached, Please find the LOGO file and some sample, we new design with much better look than those samples.

```html
<!DOCTYPE html>
<html lang="en">
<head>
<meta charset="utf-8">
<title>VIP Golden Card</title>
<link rel="stylesheet" href="https://fonts.googleapis.com/css2?family=Jost:wght@300;400&family=Lato:wght@400&family=Cinzel:wght@400&display=swap">
<style>
  :root {
    --page: #ffffff;
    --gold-dark: #9c7a3c;
    --gold-mid: #d6b574;
    --gold-light: #f3e2b6;
    --gold-text: #c9a45c;
    --ink: #1a1a1a;
    --panel: #0b0b0b;
    --strip: #bdbdbd;
    --strip-edge: #e8e8e8;
  }
  * { margin: 0; padding: 0; box-sizing: border-box; }
  html, body { width: 1200px; height: 960px; overflow: hidden; background: var(--page); }
  .canvas { position: relative; width: 1200px; height: 960px; }

  .series-title {
    position: absolute; left: 92px; top: 76px;
    display: flex; align-items: center; gap: 22px;
    color: var(--gold-text);
    font-family: "Jost", sans-serif; font-weight: 300;
  }
  .series-title__main { font-size: 46px; letter-spacing: 5px; line-height: 1; }
  .series-title__sub { font-size: 18px; letter-spacing: 2.5px; line-height: 20px; }

  .card {
    position: absolute; left: 341px; width: 518px; height: 288px;
    box-shadow: 0 14px 12px -10px rgba(0,0,0,0.35);
  }
  .card--front { top: 121px; }
  .card--back { top: 532px; }
  .card__surface {
    position: absolute; inset: 0;
    background:
      linear-gradient(100deg, rgba(255,255,255,0) 20%, rgba(255,250,230,0.45) 42%, rgba(255,255,255,0) 60%),
      linear-gradient(160deg, var(--gold-light) 0%, var(--gold-mid) 35%, var(--gold-dark) 62%, var(--gold-mid) 80%, var(--gold-light) 100%);
  }

  .badge {
    position: absolute; left: 154px; top: 40px; width: 211px; height: 210px;
    background: var(--panel);
    padding: 7px;
  }
  .badge__frame {
    width: 100%; height: 100%;
    border: 2px solid var(--gold-text);
    display: flex; flex-direction: column; align-items: center; justify-content: center;
    color: var(--gold-text);
  }
  .badge__name {
    font-family: "Lato", sans-serif; font-size: 18px; letter-spacing: 0.5px;
    text-align: center; line-height: 1.25;
  }
  .badge__level {
    font-family: "Cinzel", serif; font-size: 24px; margin-top: 22px; line-height: 1;
  }
  .badge__number {
    font-family: "Jost", sans-serif; font-size: 14px; letter-spacing: 3px; margin-top: 6px;
  }

  .back__heading {
    position: absolute; left: 23px; top: 22px;
    font-family: "Lato", sans-serif; font-weight: 400; font-size: 21px; color: var(--ink);
  }
  .back__signature {
    position: absolute; left: 19px; top: 58px; width: 371px; height: 43px;
    background: var(--strip); border: 1px solid var(--strip-edge);
  }
  .back__text {
    position: absolute; left: 53px;
    font-family: "Lato", sans-serif; font-size: 14px; line-height: 20px; color: var(--ink);
  }
  .back__note { top: 130px; }
  .back__terms { top: 167px; }
  .back__phone { top: 228px; }
</style>
</head>
<body>
<main class="canvas">
  <header class="series-title">
    <span class="series-title__main">VIP</span>
    <span class="series-title__sub">GOLDEN<br>CARD</span>
  </header>

  <section class="card card--front">
    <div class="card__surface" role="img" aria-label="Flowing gold wave pattern across the card"></div>
    <div class="badge">
      <div class="badge__frame">
        <p class="badge__name">Lumora Spa Resort</p>
        <p class="badge__level">VIP</p>
        <p class="badge__number">No.00018</p>
      </div>
    </div>
  </section>

  <section class="card card--back">
    <div class="card__surface" role="img" aria-label="Flowing gold wave pattern across the card"></div>
    <h2 class="back__heading">AUTHORIZE SIGNATURE</h2>
    <div class="back__signature"></div>
    <p class="back__text back__note">Please show your membership card when you check out</p>
    <p class="back__text back__terms">Signature and use of this card confirms the accecptance of the<br>Terms and Conditions of Membership</p>
    <p class="back__text back__phone">4008205566</p>
  </section>
</main>
</body>
</html>
```